Exercise Physiologist needs business cards

I have a logo, I need business cards (Sole trader) as I am moving to a new location and would like an updated look. I provide gym based exercise rehabilitation, injury prevention and movement assessments. I have over 13 years experience as an Exercise Physiologist. I would like the cards to look professional but not boring and can be a little different to stand out when sitting with other Allied Health Professional cards.

Target Market(s)

GP's, Allied health practitioners, people with injuries wanting to exercise

Industry/Entity Type

Health And Wellness

Contact Information for Business Card

Megan Dorrit - Exercise Physiologist 0437 582 906
14 Larkspur Bend Rd
North Calloway
(Door 4, Brannock Fitness)
vantorahealth@maildrop-example.com
socialpage-example.com/Vantora

Requirements
Must have
• I would like to include a section to add next appointment date and time space to the back of the card.
Nice to have
• Rounded corners and a black background on 1 or 2 sides.
Should not have
• Pictures of fit/toned bodies etc

```html
<!DOCTYPE html>
<html lang="en">
<head>
<meta charset="utf-8">
<title>Vantora Health – Business Cards</title>
<link href="https://fonts.googleapis.com/css2?family=Gochi+Hand&family=Oswald:wght@300;400;500&display=swap" rel="stylesheet">
<style>
  :root{
    --bg:#2b2e33;
    --card:#ffffff;
    --edge:#d9dde3;
    --brand:#2e63b8;
    --brand-light:#5a8fd8;
    --dot-fill:#a9c8ef;
    --ink:#2a2c30;
    --rule:#6f9ad6;
  }
  *{box-sizing:border-box;margin:0;padding:0}
  html,body{width:1200px;height:900px;overflow:hidden;background:var(--bg)}
  .stage{position:relative;width:1200px;height:900px}
  .card{position:absolute;top:280px;width:560px;height:340px;border-radius:28px;background:var(--card);overflow:hidden;box-shadow:0 18px 40px rgba(0,0,0,.45),0 0 0 1px var(--edge)}
  .card--front{left:20px}
  .card--back{left:620px}

  /* front */
  .front-band{position:absolute;left:0;top:0;width:100%;height:132px;background:var(--brand)}
  .front-band__pointer{position:absolute;left:420px;top:132px;width:0;height:0;border-left:16px solid transparent;border-right:16px solid transparent;border-top:16px solid var(--brand)}
  .holder{position:absolute;right:44px;top:28px;text-align:left;color:#fff}
  .holder__name{font-family:"Gochi Hand",cursive;font-size:44px;line-height:1;letter-spacing:2px;text-transform:uppercase}
  .holder__role{font-family:"Oswald",sans-serif;font-weight:300;font-size:15px;letter-spacing:1px;text-transform:uppercase;margin-top:4px}
  .brand{position:absolute;left:36px;top:196px;display:flex;align-items:center;gap:12px}
  .brand__mark{width:54px;height:54px;border-radius:50%;background:var(--brand-light);border:4px solid var(--brand)}
  .brand__name{font-family:"Oswald",sans-serif;font-weight:400;font-size:44px;color:var(--brand);line-height:1}
  .contact{position:absolute;left:330px;top:176px;font-family:"Oswald",sans-serif;font-weight:300;font-size:16px;line-height:1.45;color:var(--ink);text-transform:uppercase;letter-spacing:.5px;font-style:normal}
  .contact__phone{margin-bottom:12px}

  /* back */
  .back-art{position:absolute;inset:0;width:560px;height:340px}
  .appt-title{font-family:"Oswald",sans-serif;font-weight:500;font-size:26px;letter-spacing:6px;fill:#fff}
  .appt-label{font-family:"Oswald",sans-serif;font-weight:400;font-size:13px;fill:var(--ink);text-transform:uppercase}
  .appt-day{fill:var(--dot-fill);stroke:var(--brand);stroke-width:3}
  .appt-rule{stroke:var(--rule);stroke-width:1.2}
</style>
</head>
<body>
<main class="stage">

  <section class="card card--front" aria-label="Business card front">
    <div class="front-band"></div>
    <div class="front-band__pointer"></div>
    <div class="holder">
      <p class="holder__name">Megan Dorrit</p>
      <p class="holder__role">Exercise Physiologist</p>
    </div>
    <div class="brand">
      <span class="brand__mark"></span>
      <span class="brand__name">vantora</span>
    </div>
    <address class="contact">
      <p class="contact__phone">0437 582 906</p>
      <p>14 Larkspur Bend Rd</p>
      <p>North Calloway</p>
      <p>(Door 4, Brannock Fitness)</p>
    </address>
  </section>

  <section class="card card--back" aria-label="Business card back – next appointment">
    <svg class="back-art" viewBox="0 0 560 340" xmlns="http://www.w3.org/2000/svg">
      <rect class="appt-band" x="0" y="0" width="560" height="100" fill="var(--brand)"/>
      <polygon points="340,100 372,100 356,116" fill="var(--brand)"/>
      <text class="appt-title" x="530" y="62" text-anchor="end">NEXT APPOINTMENT</text>

      <g class="appt-days">
        <circle class="appt-day" cx="80" cy="140" r="13"/>
        <text class="appt-label" x="80" y="170" text-anchor="middle">Mon</text>
        <circle class="appt-day" cx="150" cy="164" r="13"/>
        <text class="appt-label" x="150" y="194" text-anchor="middle">Tue</text>
        <circle class="appt-day" cx="220" cy="188" r="13"/>
        <text class="appt-label" x="220" y="218" text-anchor="middle">Wed</text>
        <circle class="appt-day" cx="290" cy="212" r="13"/>
        <text class="appt-label" x="290" y="242" text-anchor="middle">Thu</text>
        <circle class="appt-day" cx="360" cy="236" r="13"/>
        <text class="appt-label" x="360" y="266" text-anchor="middle">Fri</text>
        <circle class="appt-day" cx="430" cy="260" r="13"/>
        <text class="appt-label" x="430" y="290" text-anchor="middle">Sat</text>
      </g>

      <g class="appt-fields">
        <text class="appt-label" x="30" y="224">Date</text>
        <line class="appt-rule" x1="30" y1="232" x2="262" y2="232"/>
        <line class="appt-rule" x1="150" y1="276" x2="334" y2="276"/>
        <text class="appt-label" x="240" y="296" text-anchor="middle">Time</text>
        <line class="appt-rule" x1="300" y1="310" x2="470" y2="310"/>
        <text class="appt-label" x="385" y="330" text-anchor="middle">PM/AM</text>
      </g>
    </svg>
  </section>

</main>
</body>
</html>
```